Lanterne architecture business cards

We are a new company based in New Zealand. We Specialize in High end Luxury Residential Architecture.

Every home is bespoke and is designed to each clients individual requirements and needs.

I like to design buildings that inspire people through light and form while offering a high level of comfort and usability.

Lines of sight, proportion and balance are fundamental to the spaces I create.
Updates

August 5th is current deadline - Today's date is the 13th of August.

Target Market(s)

New Zealanders who want a custom individual home design, typically 30-65 year old males and females

Industry/Entity Type

Architecture

Contact Information for Business Card

Director - Derek Tolson
Contact Number - 0279164073
Email - info@lanternearchitecture-example.co.nz
Webstie - www.lanternearchitecture-example.co.nz
Social Media - @lanternearchitecture

Font styles to use
Sans Serif

Requirements
Must have
• Logo (Both Sides)
Website
Email
Contact Number
Social Media

Nice to have
• Texture
Should not have
• More than 3 colours - typically I would've thought 2 would be good to match the logo.

```html
<!DOCTYPE html>
<html lang="en">
<head>
<meta charset="utf-8">
<title>Lanterne Architecture – Business Cards</title>
<link href="https://fonts.googleapis.com/css2?family=Bitter:wght@400;500&display=swap" rel="stylesheet">
<style>
  :root {
    --teal-deep: #2a8a99;
    --teal: #348f9d;
    --ink: #111111;
    --muted: #6d6d6d;
    --white: #ffffff;
    --plan-line: rgba(160, 170, 175, 0.14);
    --plan-line-on-teal: rgba(255, 255, 255, 0.10);
  }
  * { margin: 0; padding: 0; box-sizing: border-box; }
  html, body { width: 1050px; height: 1200px; overflow: hidden; background: var(--white); }
  body { position: relative; font-family: 'Bitter', Georgia, serif; color: var(--ink); }

  .plan-texture { position: absolute; }
  .plan-texture--back {
    left: 576px; top: 0; width: 474px; height: 560px;
    background: radial-gradient(ellipse at 55% 45%, var(--plan-line) 0%, rgba(160,170,175,0.05) 60%, transparent 78%);
  }
  .plan-texture--front {
    left: 470px; top: 650px; width: 480px; height: 545px;
    background: radial-gradient(ellipse at 50% 45%, var(--plan-line-on-teal) 0%, rgba(255,255,255,0.04) 60%, transparent 80%);
  }

  .card-front-square {
    position: absolute; left: 0; top: 0; width: 394px; height: 471px;
    background: var(--teal-deep);
  }
  .edge-bar {
    position: absolute; left: 394px; top: 151px; width: 10px; height: 210px;
    background: var(--ink);
  }

  .brand { position: absolute; text-align: center; color: var(--white); font-weight: 400; }
  .brand__mark { display: block; margin: 0 auto; }
  .brand__name { display: block; text-transform: uppercase; white-space: nowrap; }
  .brand__tag  { display: block; text-transform: uppercase; white-space: nowrap; }

  .brand--small { left: 0; width: 394px; top: 176px; }
  .brand--small .brand__mark { width: 44px; height: 44px; margin-bottom: 18px; }
  .brand--small .brand__name { font-size: 19px; letter-spacing: 14px; padding-left: 14px; line-height: 22px; }
  .brand--small .brand__tag  { font-size: 6.5px; letter-spacing: 13.5px; padding-left: 13.5px; margin-top: 3px; }

  .contact-side { position: absolute; right: 281px; top: 80px; text-align: right; }
  .contact-side__name { font-size: 27px; font-weight: 500; letter-spacing: 2px; text-transform: uppercase; line-height: 32px; }
  .contact-side__role { font-size: 11px; letter-spacing: 1.5px; color: var(--muted); text-transform: uppercase; margin-top: 2px; }

  .contact-list { position: absolute; right: 280px; top: 188px; list-style: none; }
  .contact-list__item { height: 37px; display: flex; justify-content: flex-end; align-items: center; font-size: 15px; position: relative; }
  .contact-list__item:nth-child(4) { margin-top: 2px; }
  .contact-list__icon { position: absolute; left: calc(100% + 37px); width: 29px; height: 29px; }

  .card-front-wide {
    position: absolute; left: 68px; top: 568px; width: 831px; height: 498px;
    background: var(--teal);
  }
  .brand--large { left: 68px; width: 831px; top: 729px; }
  .brand--large .brand__mark { width: 82px; height: 82px; margin-bottom: 26px; margin-left: 380px; }
  .brand--large .brand__name { font-size: 36px; letter-spacing: 23px; padding-left: 23px; line-height: 40px; }
  .brand--large .brand__tag  { font-size: 10px; letter-spacing: 27px; padding-left: 27px; margin-top: 8px; }
</style>
</head>
<body>

  <div class="plan-texture plan-texture--back" role="img" aria-label="Faint architectural floor plan texture behind the contact side"></div>

  <section class="card-front-square">
  </section>
  <div class="edge-bar"></div>
  <div class="brand brand--small">
    <svg class="brand__mark" viewBox="0 0 44 44" aria-hidden="true"><circle cx="22" cy="22" r="19" fill="none" stroke="#ffffff" stroke-width="4"/></svg>
    <span class="brand__name">Lanterne</span>
    <span class="brand__tag">Architecture</span>
  </div>

  <section class="contact-side">
    <h1 class="contact-side__name">Derek Tolson</h1>
    <p class="contact-side__role">Director</p>
  </section>

  <ul class="contact-list">
    <li class="contact-list__item">0279 164073
      <svg class="contact-list__icon" viewBox="0 0 30 30" aria-hidden="true"><circle cx="15" cy="15" r="13.5" fill="none" stroke="#111" stroke-width="1.5"/><rect x="10.5" y="7.5" width="9" height="15" rx="1.5" fill="none" stroke="#111" stroke-width="1.5"/><line x1="13.5" y1="20" x2="16.5" y2="20" stroke="#111" stroke-width="1.2"/></svg>
    </li>
    <li class="contact-list__item">info@lanternearchitecture-example.co.nz
      <svg class="contact-list__icon" viewBox="0 0 30 30" aria-hidden="true"><circle cx="15" cy="15" r="13.5" fill="none" stroke="#111" stroke-width="1.5"/><rect x="8.5" y="10.5" width="13" height="9" rx="1" fill="#111"/><polyline points="8.5,11 15,16 21.5,11" fill="none" stroke="#fff" stroke-width="1.2"/></svg>
    </li>
    <li class="contact-list__item">www.lanternearchitecture-example.co.nz
      <svg class="contact-list__icon" viewBox="0 0 30 30" aria-hidden="true"><circle cx="15" cy="15" r="13.5" fill="none" stroke="#111" stroke-width="1.5"/><circle cx="15" cy="15" r="7" fill="none" stroke="#111" stroke-width="1.3"/><ellipse cx="15" cy="15" rx="3" ry="7" fill="none" stroke="#111" stroke-width="1.1"/><line x1="8" y1="15" x2="22" y2="15" stroke="#111" stroke-width="1.1"/><line x1="9" y1="11.5" x2="21" y2="11.5" stroke="#111" stroke-width="1"/><line x1="9" y1="18.5" x2="21" y2="18.5" stroke="#111" stroke-width="1"/></svg>
    </li>
    <li class="contact-list__item">@lanternearchitecture
      <svg class="contact-list__icon" viewBox="0 0 30 30" aria-hidden="true"><circle cx="15" cy="15" r="13.5" fill="none" stroke="#111" stroke-width="1.5"/></svg>
    </li>
  </ul>

  <section class="card-front-wide"></section>
  <div class="plan-texture plan-texture--front" role="img" aria-label="Faint architectural floor plan texture across the card front"></div>
  <div class="brand brand--large">
    <svg class="brand__mark" viewBox="0 0 82 82" aria-hidden="true"><circle cx="41" cy="41" r="36" fill="none" stroke="#ffffff" stroke-width="7"/></svg>
    <span class="brand__name">Lanterne</span>
    <span class="brand__tag">Architecture</span>
  </div>

</body>
</html>
```